Business Card - connecting 2 souls and beggining the journey of self discovery

Logo on the front
with tag line

On the back list of services and contact details

Seminars
workshops
Coaching
podcasts

Daniel Porthwick
Health & Wellbeing Life Coach
0491 372 815
daniel@wovenpathwellness.example
wovenpathwellness.example

Industry/Entity Type

Life Coaching

Contact Information for Business Card

I like the use of colour from the logo to be used. I'm not a fan of white.

Requirements
Must have
• My tagline: The journey home starts with you
Nice to have
• Use of colour that is in the mind body soul logo

```html
<!DOCTYPE html>
<html lang="en">
<head>
<meta charset="utf-8">
<title>Woven Path Wellness – Business Card</title>
<link rel="stylesheet" href="https://fonts.googleapis.com/css2?family=Varela+Round&display=swap">
<style>
  :root {
    --backdrop: #5f6a70;
    --card: #f3ecf8;
    --purple: #7b4ba6;
    --purple-fade: rgba(123, 75, 166, 0);
    --brand-grey: #6f6b75;
    --ink: #1f1f22;
    --mark: #8a55b5;
    --white: #ffffff;
  }
  * { box-sizing: border-box; margin: 0; padding: 0; }
  html, body {
    width: 1200px;
    height: 900px;
    overflow: hidden;
  }
  body {
    background: var(--backdrop);
    font-family: "Varela Round", "Helvetica Neue", Arial, sans-serif;
    position: relative;
  }
  .card {
    position: absolute;
    left: 340px;
    width: 520px;
    height: 300px;
    background: var(--card);
    border-radius: 16px;
    overflow: hidden;
  }
  .card--front { top: 110px; }
  .card--back  { top: 490px; }

  /* Front */
  .front-lockup {
    position: absolute;
    inset: 0;
    display: flex;
    flex-direction: column;
    align-items: center;
    justify-content: center;
  }
  .brand-dot {
    width: 84px;
    height: 84px;
    border-radius: 50%;
    background: var(--mark);
    flex: none;
  }
  .brand-name {
    color: var(--brand-grey);
    font-size: 34px;
    letter-spacing: -0.5px;
    white-space: nowrap;
  }
  .front-lockup .brand-name { margin-top: 22px; }
  .tagline {
    margin-top: 10px;
    color: var(--purple);
    font-size: 15px;
    letter-spacing: 0.3px;
    white-space: nowrap;
  }

  /* Back */
  .service-band {
    position: absolute;
    left: 0;
    top: 0;
    width: 220px;
    height: 230px;
    background: linear-gradient(120deg, var(--purple) 0%, rgba(123,75,166,0.55) 45%, var(--purple-fade) 100%);
  }
  .service-list {
    position: absolute;
    left: 26px;
    top: 24px;
    list-style: none;
    color: var(--white);
    font-size: 13px;
    line-height: 20px;
  }
  .service-list li {
    display: flex;
    align-items: center;
    gap: 9px;
  }
  .service-list li::before {
    content: "";
    width: 7px;
    height: 7px;
    border-radius: 50%;
    background: var(--white);
  }
  .back-brand {
    position: absolute;
    right: 26px;
    top: 32px;
    display: flex;
    align-items: center;
    gap: 14px;
  }
  .back-brand .brand-dot { width: 46px; height: 46px; }
  .back-brand .brand-name { font-size: 20px; }

  .contact-block {
    position: absolute;
    left: 262px;
    top: 126px;
  }
  .person-name {
    color: var(--purple);
    font-size: 25px;
    line-height: 30px;
    white-space: nowrap;
  }
  .person-role {
    color: var(--ink);
    font-size: 11.5px;
    margin-bottom: 14px;
  }
  .contact-list {
    list-style: none;
    color: var(--ink);
    font-size: 12px;
    line-height: 19px;
  }
  .contact-list li {
    display: flex;
    align-items: center;
    gap: 7px;
    white-space: nowrap;
  }
  .contact-list svg { width: 11px; height: 11px; flex: none; }
</style>
</head>
<body>

  <section class="card card--front" aria-label="Card front">
    <div class="front-lockup">
      <span class="brand-dot"></span>
      <span class="brand-name">Woven Path Wellness</span>
      <span class="tagline">The journey home starts with you</span>
    </div>
  </section>

  <section class="card card--back" aria-label="Card back">
    <div class="service-band"></div>
    <ul class="service-list">
      <li>Seminars</li>
      <li>Workshops</li>
      <li>Coaching</li>
      <li>Podcasts</li>
    </ul>

    <div class="back-brand">
      <span class="brand-name">Woven Path Wellness</span>
      <span class="brand-dot"></span>
    </div>

    <div class="contact-block">
      <p class="person-name">Daniel Porthwick</p>
      <p class="person-role">Health &amp; Wellbeing Life Coach</p>
      <ul class="contact-list">
        <li>
          <svg viewBox="0 0 12 12" aria-hidden="true"><path d="M3 1 L5 3.4 L4 4.6 Q5 7 7.4 8 L8.6 7 L11 9 L9.6 11 Q4.5 10.5 1 3 Z" fill="#7b4ba6"/></svg>
          0491 372 815
        </li>
        <li>
          <svg viewBox="0 0 12 12" aria-hidden="true"><rect x="1" y="2.5" width="10" height="7" fill="#7b4ba6"/><path d="M1 2.5 L6 6.5 L11 2.5" stroke="#fff" stroke-width="1" fill="none"/></svg>
          daniel@wovenpathwellness.example
        </li>
        <li>
          <svg viewBox="0 0 12 12" aria-hidden="true"><circle cx="6" cy="6" r="4.8" fill="none" stroke="#7b4ba6" stroke-width="1.2"/><path d="M1.2 6 H10.8 M6 1.2 Q3 6 6 10.8 M6 1.2 Q9 6 6 10.8" stroke="#7b4ba6" stroke-width="0.9" fill="none"/></svg>
          wovenpathwellness.example
        </li>
      </ul>
    </div>
  </section>

</body>
</html>
```